Werbeplakat für Frisörsalon
Zielgruppe
Frisörsalon (Coiffeursalon Lindenhof) mit hohem Qualitätsstandard im mittel-hohem Preissegment. Zielgruppe hauptsächlich Frauen (20j - 40j). Jedoch bieten wir auch Herrenfrisuren an.
Aufgabenstellung
Format --> A1
auf erstem Blick erkennbar das es sich um einen Frisörsalon handelt
Text:
erstklassige Damen- und Herrenfrisuren
moderne Kinderfrisuren
Waschen, Schneiden, Föhnen
Färben, Tönung, Mèches
VERANTIQ Behandlung
Hochstecken / Hochzeitsfrisuren / Gala
Warme Farben
Logo auf dem Plakat in Originalfarben
Dame auf dem Plakat mit langem lockigem dichtem Haar (Rotschopf)

```html
<!DOCTYPE html>
<html lang="de">
<head>
<meta charset="utf-8">
<title>Coiffeursalon Lindenhof – Plakat</title>
<link href="https://fonts.googleapis.com/css2?family=Ubuntu:wght@400;500;700&display=swap" rel="stylesheet">
<style>
  :root {
    --maroon: #6e0606;
    --cream: #fde5c8;
    --cream-text: #fde3c4;
    --photo-light: #e9b47c;
    --photo-mid: #c9703a;
    --photo-red: #a5141e;
    --photo-dark: #4a3329;
  }
  * { margin: 0; padding: 0; box-sizing: border-box; }
  html, body { width: 938px; height: 1200px; overflow: hidden; background: var(--cream); }
  .poster {
    position: relative;
    width: 938px;
    height: 1200px;
    background: var(--cream);
    font-family: "Ubuntu", sans-serif;
    color: var(--maroon);
    overflow: hidden;
  }
  .poster__art { position: absolute; inset: 0; }
  .brand {
    position: absolute;
    top: 688px;
    left: 0;
    width: 938px;
    text-align: center;
    font-size: 44px;
    line-height: 52px;
    font-weight: 500;
    color: var(--maroon);
    letter-spacing: 0.5px;
  }
  .services {
    position: absolute;
    top: 776px;
    left: 0;
    width: 938px;
    list-style: none;
    text-align: center;
    font-size: 31px;
    line-height: 43.5px;
  }
  .services strong { font-weight: 700; }
  .contact-band {
    position: absolute;
    left: 0;
    top: 1050px;
    width: 938px;
    height: 150px;
    background: var(--maroon);
    color: var(--cream-text);
    text-align: center;
  }
  .contact-band__address {
    padding-top: 18px;
    font-size: 38px;
    letter-spacing: 0.5px;
  }
  .contact-band__phone {
    font-size: 72px;
    line-height: 80px;
    letter-spacing: 1px;
  }
</style>
</head>
<body>
<div class="poster">
  <svg class="poster__art" width="938" height="1200" viewBox="0 0 938 1200">
    <defs>
      <linearGradient id="photoTone" x1="0" y1="0" x2="1" y2="0">
        <stop offset="0" stop-color="var(--photo-light)"/>
        <stop offset="0.22" stop-color="var(--photo-dark)"/>
        <stop offset="0.38" stop-color="var(--photo-red)"/>
        <stop offset="0.55" stop-color="var(--photo-mid)"/>
        <stop offset="0.8" stop-color="#8a5a3c"/>
        <stop offset="1" stop-color="var(--photo-light)"/>
      </linearGradient>
    </defs>
    <rect class="hero-photo" x="0" y="0" width="938" height="760" fill="url(#photoTone)"
          role="img" aria-label="Foto: Frau mit dichtem, lockigem Haar in Schwarz-, Rot-, Kupfer- und Brauntönen vor warmem Hintergrund"/>
    <path class="wave wave--maroon" d="M0 722 C 200 640, 380 508, 500 508 C 640 508, 730 680, 938 678 L938 1200 L0 1200 Z" fill="var(--maroon)"/>
    <path class="wave wave--cream" d="M0 745 C 220 670, 400 568, 520 568 C 660 568, 740 700, 938 696 L938 1200 L0 1200 Z" fill="var(--cream)"/>
    <rect class="deco-scissors deco-scissors--left" x="0" y="860" width="190" height="160" rx="20" fill="var(--maroon)" opacity="0.12"
          role="img" aria-label="Dekoration: geöffnete Schere links"/>
    <rect class="deco-scissors deco-scissors--right" x="760" y="740" width="178" height="220" rx="20" fill="var(--maroon)" opacity="0.12"
          role="img" aria-label="Dekoration: geöffnete Schere rechts"/>
  </svg>

  <div class="brand">Coiffeursalon Lindenhof</div>

  <ul class="services">
    <li>Erstklassige Damen- und Herrenfrisuren</li>
    <li>moderne Kinderfrisuren</li>
    <li>Waschen, Schneiden, Föhnen</li>
    <li>Färben, Tönung, Mèches</li>
    <li><strong>VERANTIQ</strong> Behandlung</li>
    <li>Hochstecken / Hochzeitsfrisuren / Gala</li>
  </ul>

  <div class="contact-band">
    <p class="contact-band__address">LINDENWEG 12 | 3072 OSTERMUNDIGEN</p>
    <p class="contact-band__phone">031 555 18 27</p>
  </div>
</div>
</body>
</html>
```